上記商品のインバウンド向けにも対応できるパッケージを依頼いたします。既存パッケージはどちらかと言うとポップな感じで高級感からは程遠いデザインなのですが、今回は高級志向で「和」のお土産品としても手に取っていただけるようなデザインを希望いたします。「ふわりんポンポン」と言う名称も変更いただいて構いません。
サイズ:65×100mm
青系
• イラストレーター形式 (.ai)
①参考までに海外ではからすみはbottargaと言う名称で通っているようです。インバウンドも 対象に入れたいので、その辺りもご検討いただけますと嬉しいです。
②弊社所在地が宮崎県の北部に当たり、高千穂まで1時間足らずの場所に会社がございます。
高千穂の神水流れる日向灘沖で獲れた原料を使っておりますので、そのあたりもデザインに取り込んでいただけると海外向けにもウケるのでは?と考えております。
すみません、商品の中身を提示しておりませんでしたので画像を追加いたします。

弊社の思い描く高級感が反映されたデザインでした。また、大きな目的である「インバウンド向け」と言った点で、漢字を大きく配置してくださった点が素晴らしかったです。追加でのご依頼でデザインを崩さずに宮崎感を出していただき、最終的に決定とさせていただきました。

ご提案いただきましたピクセラーの皆様、本当にお忙しい中ありがとうございました。
応募スタート時より素敵なデザインがたくさん集まり、最後の最後までスタッフ一同頭を悩ませた
結果期間ギリギリでの選定とさせていただきました。これからも新商品を予定しており、またその際は応募を考えております。また皆様のお力をお貸しいただければ幸甚です。
スタッフ一同感謝申し上げます。

```html
<!DOCTYPE html>
<html lang="ja">
<head>
<meta charset="utf-8">
<title>唐墨 BOTTARGA パッケージ</title>
<link rel="stylesheet" href="https://fonts.googleapis.com/css2?family=Shippori+Mincho+B1:wght@800&family=Noto+Serif+JP:wght@500;700&display=swap">
<style>
  :root {
    --stage: #ececec;
    --card: #ffffff;
    --ink: #26318c;
    --ink-mid: #aab3dc;
    --seal: #d7252d;
    --trim: #8a8a8a;
  }
  html, body {
    margin: 0;
    padding: 0;
    overflow: hidden;
    background: var(--stage);
  }
  .canvas {
    width: 887px;
    height: 1200px;
    display: block;
  }
  .trim-mark { stroke: var(--trim); stroke-width: 1.2; fill: none; }
  .card { fill: var(--card); }
  .frame-outer { fill: none; stroke: var(--ink); stroke-width: 9; }
  .frame-inner { fill: none; stroke: var(--ink); stroke-width: 3; }
  .panel { fill: none; stroke: var(--ink); stroke-width: 5; }
  .label-latin {
    font-family: "Noto Serif JP", "Times New Roman", serif;
    font-weight: 500;
    font-size: 34px;
    letter-spacing: 3px;
    fill: var(--ink);
  }
  .title-kanji {
    font-family: "Shippori Mincho B1", serif;
    font-weight: 800;
    font-size: 200px;
    fill: var(--ink);
  }
  .title-kana {
    font-family: "Noto Serif JP", serif;
    font-weight: 700;
    font-size: 32px;
    letter-spacing: 3px;
    fill: var(--ink);
  }
  .brand-mark { fill: var(--seal); }
  .brand-name {
    font-family: "Noto Serif JP", serif;
    font-weight: 700;
    font-size: 24px;
    fill: var(--seal);
  }
  .illustration { fill: url(#scene-tone); }
  .pattern-block { fill: var(--ink-mid); }
</style>
</head>
<body>
<svg class="canvas" viewBox="0 0 887 1200" xmlns="http://www.w3.org/2000/svg">
  <defs>
    <linearGradient id="scene-tone" x1="0" y1="0" x2="0" y2="1">
      <stop offset="0" stop-color="#e6e9f6"/>
      <stop offset="1" stop-color="#c9d0ec"/>
    </linearGradient>
    <clipPath id="panel-clip">
      <rect x="186" y="262" width="515" height="726" rx="200"/>
    </clipPath>
    <path id="arc-top" d="M 290 270 A 230 230 0 0 1 597 270"/>
    <path id="arc-bottom" d="M 290 1000 A 230 230 0 0 0 597 1000"/>
  </defs>

  <g class="trim-marks">
    <path class="trim-mark" d="M89 0 V60 M0 83 H66 M30 0 V60 M0 30 H66"/>
    <path class="trim-mark" d="M798 0 V60 M887 83 H821 M857 0 V60 M887 30 H821"/>
    <path class="trim-mark" d="M89 1200 V1140 M0 1124 H66 M30 1200 V1140 M0 1170 H66"/>
    <path class="trim-mark" d="M798 1200 V1140 M887 1124 H821 M857 1200 V1140 M887 1170 H821"/>
    <path class="trim-mark" d="M443 0 V50 M443 1200 V1150 M0 600 H50 M887 600 H837"/>
  </g>

  <rect class="card" x="89" y="83" width="709" height="1041"/>

  <rect class="pattern-block" x="96" y="180" width="44" height="60" role="img" aria-label="Blue checkered square accent"/>
  <rect class="pattern-block" x="748" y="945" width="44" height="70" role="img" aria-label="Blue checkered square accent"/>

  <rect class="frame-outer" x="140" y="140" width="607" height="955" rx="250"/>
  <rect class="frame-inner" x="156" y="156" width="575" height="923" rx="236"/>

  <g clip-path="url(#panel-clip)">
    <rect class="illustration" x="186" y="262" width="300" height="726"
          role="img" aria-label="Line illustration of a mullet standing upright with rising sun, clouds and breaking waves of the Hyuga sea"/>
  </g>
  <rect class="panel" x="186" y="262" width="515" height="726" rx="200"/>

  <text class="label-latin" text-anchor="middle"><textPath href="#arc-top" startOffset="50%">BOTTARGA</textPath></text>
  <text class="label-latin" text-anchor="middle"><textPath href="#arc-bottom" startOffset="50%">KARASUMI</textPath></text>

  <g class="title">
    <text class="title-kanji" x="560" y="465" text-anchor="middle">唐</text>
    <text class="title-kana" x="560" y="508" text-anchor="middle">からすみ</text>
    <text class="title-kanji" x="560" y="698" text-anchor="middle">墨</text>
  </g>

  <g class="brand">
    <rect class="brand-mark" x="598" y="760" width="56" height="56"/>
    <text class="brand-name" x="626" y="850" text-anchor="middle">UMINE</text>
  </g>
</svg>
</body>
</html>
```